Wordpress Corporate Website for New Business

We need a corporate website created which will act as a professional shop window for our new business. We do not need special features like merchant facilities or chatbots. The attachment shows suggested key sections as well as some possible wording. Various versions of the company logo have been attached as well to give different options to play with. We are looking for an option which is easy for us to take over and manage moving forward should we need to make minor updates.

Target Market(s)

Corporate entities

Industry/Entity Type

Private share auctions

Coding

Coded - Design and coding required

```html
<!DOCTYPE html>
<html lang="en">
<head>
<meta charset="utf-8">
<title>ShareKeel – Retain Control, Unlock Liquidity</title>
<link href="https://fonts.googleapis.com/css2?family=Poppins:wght@600;700&family=Roboto:wght@400;500;700&display=swap" rel="stylesheet">
<style>
:root{
  --purple:#8a0f96;
  --navy:#15168c;
  --ink:#1b1b1b;
  --muted:#555;
  --pink-bg:#fdf0fb;
  --team-bg:#8f1a9c;
  --support-bg:#1c1fa0;
  --footer-bg:#0b0b0b;
  --white:#fff;
}
*{box-sizing:border-box;margin:0;padding:0}
html,body{width:1200px;height:4435px;overflow:hidden}
body{font-family:"Roboto",Arial,sans-serif;color:var(--ink);background:var(--white);position:relative}
h1,h2,h3,.brand{font-family:"Poppins",Arial,sans-serif}
.btn{display:inline-flex;align-items:center;gap:10px;height:44px;padding:0 26px;border-radius:24px;color:#fff;font:700 16px "Roboto",sans-serif;text-transform:uppercase;text-decoration:none}
.btn svg{width:15px;height:15px}
.btn-purple{background:var(--purple)}
.btn-navy{background:var(--navy)}
.icon-arrow{display:inline-block}
.two-tone .a{color:var(--purple)}
.two-tone .b{color:var(--navy)}

/* header */
.site-header{height:85px;display:flex;align-items:center;padding:0 110px;justify-content:space-between}
.brand{display:flex;align-items:center;gap:10px;font-weight:700;font-size:36px;color:var(--navy)}
.brand .dot{width:32px;height:32px;border-radius:50%;background:var(--purple)}
.nav{display:flex;gap:34px;font-size:15px;font-weight:500}
.nav a{color:var(--ink);text-decoration:none}

/* hero */
.hero{position:relative;height:647px}
.hero-photo{position:absolute;inset:0;background:linear-gradient(90deg,#3f4448 0%,#6f757a 35%,#a9adb0 60%,#d9dcde 100%)}
.hero-copy{position:absolute;left:107px;top:212px}
.hero h1{color:#fff;font-size:58px;line-height:66px;font-weight:700}
.hero .btn{margin-top:34px;height:46px}

/* about */
.about{height:552px;position:relative}
.about-emblem{position:absolute;left:165px;top:96px;width:365px;height:365px;border-radius:50%;background:radial-gradient(circle at 50% 50%,#7b1aa0 0%,#4a2fb0 55%,#2a24a0 100%)}
.about-copy{position:absolute;left:615px;top:130px;width:425px}
.about h2{font-size:40px;color:var(--purple);font-weight:700;margin-bottom:14px}
.about p{font-size:15px;line-height:28.5px;color:#333;text-align:justify}
.about .btn{margin-top:28px}

/* features */
.features{height:509px;background:var(--pink-bg);position:relative}
.section-title{text-align:center;font-size:38px;font-weight:700}
.features .section-title{padding-top:80px}
.feature-card{position:absolute;top:171px;width:474px;height:247px;background:#fff;box-shadow:0 2px 10px rgba(0,0,0,.12);display:flex;padding:30px 26px}
.feature-icon{flex:none;width:82px;height:82px;border-radius:50%;background:#fff;box-shadow:0 2px 10px rgba(0,0,0,.15);display:flex;align-items:center;justify-content:center;margin-right:18px}
.feature-card h3{font-size:21px;font-weight:600;margin-bottom:6px}
.feature-card p{font-size:12.5px;line-height:23px;color:#444;text-align:justify}
.feature-card .btn{margin-top:14px;height:44px}

/* why choose */
.why{height:834px;position:relative}
.why .section-title{padding-top:68px}
.why-card{position:absolute;width:472px;height:221px;background:#fff;box-shadow:0 2px 10px rgba(0,0,0,.15);border-right:4px solid var(--navy);display:flex}
.why-card.alt{border-right-color:var(--purple)}
.why-photo{width:226px;height:100%;flex:none}
.why-badge{position:absolute;left:196px;top:80px;width:60px;height:60px;border-radius:50%;display:flex;align-items:center;justify-content:center;border:5px solid #fff;box-shadow:0 0 0 2px rgba(0,0,0,.08)}
.why-body{padding:30px 8px 0 36px;text-align:center;flex:1}
.why-body h3{font:500 17px "Roboto",sans-serif;margin-bottom:14px}
.why-body p{font-size:14px;line-height:21.5px;color:#555;height:86px;overflow:hidden}
.why-body .more{display:inline-flex;align-items:center;gap:6px;margin-top:12px;font-weight:500;font-size:14px;color:var(--purple)}
.why-body .more svg{width:13px;height:13px}
.why .view-more{position:absolute;left:509px;top:870px}

/* team */
.team{height:583px;background:linear-gradient(90deg,#9a1fa6,#8b1a9a 60%,#86129a);color:#fff;position:relative}
.team .section-title{padding-top:70px;color:#fff}
.member{position:absolute;top:168px;width:246px;text-align:center}
.member-photo{width:206px;height:206px;border-radius:50%;border:4px solid #fff;margin:0 auto;background:linear-gradient(160deg,#c8c2bd,#8e8880)}
.member h3{font:500 17px "Roboto",sans-serif;margin-top:24px}
.member p{font-size:15px;line-height:25.5px;margin-top:8px}

/* faq */
.faq{height:535px;position:relative}
.faq .section-title{padding-top:68px}
.faq-item{position:absolute;width:468px;height:56px;border-radius:30px;background:#fff;box-shadow:0 2px 8px rgba(0,0,0,.18);display:flex;align-items:center;justify-content:space-between;padding:0 22px;font-weight:700;font-size:16px}
.faq-item svg{width:21px;height:21px}
.faq-item.active{background:var(--navy);color:#fff}

/* support */
.support{height:305px;background:var(--support-bg);color:#fff;text-align:center}
.support h2{padding-top:60px;font-size:38px;font-weight:600}
.support p{font-size:15px;line-height:26px;margin:16px auto 0;width:560px}
.support .btn{margin-top:26px}

/* footer */
.site-footer{height:385px;background:var(--footer-bg);color:#fff;position:relative;font-size:11.5px}
.footer-brand{position:absolute;left:108px;top:140px;display:flex;align-items:center;gap:10px;font:700 36px "Poppins",sans-serif;color:var(--purple)}
.footer-brand .dot{width:32px;height:32px;border-radius:50%;background:var(--navy)}
.footer-col{position:absolute;top:88px}
.footer-col h4{font:700 12.5px "Roboto",sans-serif;margin-bottom:16px}
.footer-col li{list-style:none;margin-bottom:12px}
.contact li{display:flex;gap:10px;line-height:18px;margin-bottom:14px}
.contact svg{width:12px;height:12px;flex:none;margin-top:3px}
.news p{line-height:18px;width:300px}
.news-form{display:flex;gap:6px;margin-top:16px}
.news-form span{width:273px;height:44px;border-radius:24px;background:#fff;color:#666;display:flex;align-items:center;padding-left:20px;font-size:12px}
.news-form b{width:104px;height:44px;border-radius:24px;background:var(--purple);display:flex;align-items:center;justify-content:center;font-size:15px}
.social{width:36px;height:36px;border-radius:50%;background:#2a2a2a;display:flex;align-items:center;justify-content:center;margin-top:18px;font-weight:700;font-size:13px}
.copyright{position:absolute;left:0;right:0;top:358px;text-align:center;font-size:11px}
</style>
</head>
<body>

<header class="site-header">
  <div class="brand"><span class="dot"></span>ShareKeel</div>
  <nav class="nav">
    <a href="#">Home</a><a href="#">About Us</a><a href="#">Our Team</a><a href="#">Key Features</a><a href="#">Why Choose</a><a href="#">Contact Us</a><a href="#">Support</a>
  </nav>
</header>

<section class="hero">
  <div class="hero-photo" role="img" aria-label="Photo of two business colleagues reviewing a document at a laptop in an office"></div>
  <div class="hero-copy">
    <h1>Retain Control,<br>Unlock Liquidity</h1>
    <a class="btn btn-purple" href="#">Get Started
      <svg viewBox="0 0 16 16"><circle cx="8" cy="8" r="8" fill="#fff"/><path d="M6.5 4.5 10 8l-3.5 3.5" stroke="#8a0f96" stroke-width="2" fill="none"/></svg></a>
  </div>
</section>

<section class="about">
  <div class="about-emblem" role="img" aria-label="Large brand emblem"></div>
  <div class="about-copy">
    <h2>About Us</h2>
    <p>At ShareKeel, we empower private companies to take control of their share transactions without the hassle of third-party involvement. Our innovative share exchange platform is designed to connect pre-approved buyers and sellers directly, fostering a secure and efficient environment for trading ownership in private enterprises.</p>
    <a class="btn btn-navy" href="#">Learn More
      <svg viewBox="0 0 16 16"><circle cx="8" cy="8" r="8" fill="#fff"/><path d="M6.5 4.5 10 8l-3.5 3.5" stroke="#15168c" stroke-width="2" fill="none"/></svg></a>
  </div>
</section>

<section class="features">
  <h2 class="section-title two-tone"><span class="a">Key</span> <span class="b">Features</span></h2>
  <article class="feature-card" style="left:110px">
    <div class="feature-icon">
      <svg width="40" height="44" viewBox="0 0 40 44"><rect x="4" y="6" width="16" height="36" fill="#15168c"/><rect x="20" y="16" width="16" height="26" fill="#8a0f96"/><g fill="#fff"><rect x="8" y="11" width="3" height="4"/><rect x="13" y="11" width="3" height="4"/><rect x="8" y="19" width="3" height="4"/><rect x="13" y="19" width="3" height="4"/><rect x="8" y="27" width="3" height="4"/><rect x="13" y="27" width="3" height="4"/><rect x="24" y="21" width="3" height="4"/><rect x="29" y="21" width="3" height="4"/><rect x="24" y="29" width="3" height="4"/><rect x="29" y="29" width="3" height="4"/></g></svg>
    </div>
    <div>
      <h3>Company</h3>
      <p>This might explain what we do to help the company roll this out and the process, including engagement with shareholders for setting up the user access, technical support provided and the information provided</p>
      <a class="btn btn-navy" href="#">Company
        <svg viewBox="0 0 16 16"><circle cx="8" cy="8" r="8" fill="#fff"/><path d="M6.5 4.5 10 8l-3.5 3.5" stroke="#15168c" stroke-width="2" fill="none"/></svg></a>
    </div>
  </article>
  <article class="feature-card" style="left:615px;align-items:flex-start;padding-top:52px">
    <div class="feature-icon">
      <svg width="48" height="44" viewBox="0 0 48 44"><circle cx="24" cy="8" r="7" fill="#8a0f96"/><g fill="#15168c"><circle cx="10" cy="26" r="4"/><circle cx="24" cy="26" r="4"/><circle cx="38" cy="26" r="4"/><path d="M3 40a7 7 0 0 1 14 0zM17 40a7 7 0 0 1 14 0zM31 40a7 7 0 0 1 14 0z"/></g></svg>
    </div>
    <div>
      <h3>Shareholder</h3>
      <p>Example of the login process, what features the platform has and what happens post a transaction.</p>
      <a class="btn btn-purple" href="#">Shareholder
        <svg viewBox="0 0 16 16"><circle cx="8" cy="8" r="8" fill="#fff"/><path d="M6.5 4.5 10 8l-3.5 3.5" stroke="#8a0f96" stroke-width="2" fill="none"/></svg></a>
    </div>
  </article>
</section>

<section class="why">
  <h2 class="section-title two-tone"><span class="a">Why Choose</span> <span class="b">ShareKeel</span></h2>

  <article class="why-card" style="left:110px;top:184px">
    <div class="why-photo" role="img" aria-label="Photo of a person using a smartphone beside a laptop" style="background:linear-gradient(135deg,#6b6f72,#a0a5a8)"></div>
    <div class="why-badge" style="background:var(--purple)"><svg width="24" height="24" viewBox="0 0 24 24"><circle cx="12" cy="12" r="9" fill="none" stroke="#fff" stroke-width="2"/><circle cx="12" cy="12" r="3" fill="#fff"/></svg></div>
    <div class="why-body"><h3>Retain Control</h3><p>Companies can maintain control over who participates in theirauctions. This control is essential for preserving</p><span class="more">LEARN MORE <svg viewBox="0 0 16 16"><circle cx="8" cy="8" r="7" fill="none" stroke="#8a0f96" stroke-width="2"/><path d="M7 5l3 3-3 3" stroke="#8a0f96" stroke-width="2" fill="none"/></svg></span></div>
  </article>

  <article class="why-card alt" style="left:615px;top:184px;border-right-color:var(--navy)">
    <div class="why-photo" role="img" aria-label="Photo of a trader pointing at market charts on monitors" style="background:linear-gradient(135deg,#3c4248,#8d959c)"></div>
    <div class="why-badge" style="background:var(--navy)"><svg width="24" height="24" viewBox="0 0 24 24"><path d="M12 3c3 3 3 9 0 14-3-5-3-11 0-14z" fill="#fff"/><circle cx="6" cy="18" r="3" fill="none" stroke="#fff" stroke-width="1.6"/><circle cx="18" cy="18" r="3" fill="none" stroke="#fff" stroke-width="1.6"/></svg></div>
    <div class="why-body"><h3>Unlock Liquidity</h3><p>ShareKeel provides a structured marketplace which facilitates efficient and easy share transactions, creating</p><span class="more" style="color:var(--navy)">LEARN MORE <svg viewBox="0 0 16 16"><circle cx="8" cy="8" r="7" fill="none" stroke="#15168c" stroke-width="2"/><path d="M7 5l3 3-3 3" stroke="#15168c" stroke-width="2" fill="none"/></svg></span></div>
  </article>

  <article class="why-card" style="left:110px;top:433px">
    <div class="why-photo" role="img" aria-label="Photo of a small model house on documents" style="background:linear-gradient(135deg,#e08a3a,#6b4a36)"></div>
    <div class="why-badge" style="background:var(--navy)"><svg width="24" height="24" viewBox="0 0 24 24"><rect x="4" y="6" width="16" height="12" rx="2" fill="none" stroke="#fff" stroke-width="2"/><circle cx="12" cy="12" r="3" fill="#fff"/></svg></div>
    <div class="why-body"><h3>Direct Transactions</h3><p>Say goodbye to intermediaries. Our platform enables shareholders in private companies to trade</p><span class="more" style="color:var(--navy)">LEARN MORE <svg viewBox="0 0 16 16"><circle cx="8" cy="8" r="7" fill="none" stroke="#15168c" stroke-width="2"/><path d="M7 5l3 3-3 3" stroke="#15168c" stroke-width="2" fill="none"/></svg></span></div>
  </article>

  <article class="why-card alt" style="left:615px;top:433px">
    <div class="why-photo" role="img" aria-label="Photo of hands holding a glowing digital shape" style="background:linear-gradient(135deg,#10202e,#2f5a72)"></div>
    <div class="why-badge" style="background:var(--purple)"><svg width="24" height="24" viewBox="0 0 24 24"><circle cx="12" cy="12" r="3" fill="#fff"/><g stroke="#fff" stroke-width="1.6"><path d="M12 2v5M12 17v5M2 12h5M17 12h5M5 5l3.5 3.5M15.5 15.5 19 19M19 5l-3.5 3.5M8.5 15.5 5 19"/></g></svg></div>
    <div class="why-body"><h3>Scalability</h3><p>The ShareKeel platform can scale to accommodate the needs of companies of varying sizes, from startups to</p><span class="more">LEARN MORE <svg viewBox="0 0 16 16"><circle cx="8" cy="8" r="7" fill="none" stroke="#8a0f96" stroke-width="2"/><path d="M7 5l3 3-3 3" stroke="#8a0f96" stroke-width="2" fill="none"/></svg></span></div>
  </article>

  <a class="btn btn-purple view-more" href="#" style="top:713px;left:509px">View More
    <svg viewBox="0 0 16 16"><circle cx="8" cy="8" r="8" fill="#fff"/><path d="M6.5 4.5 10 8l-3.5 3.5" stroke="#8a0f96" stroke-width="2" fill="none"/></svg></a>
</section>

<section class="team">
  <h2 class="section-title">Our Team</h2>
  <div class="member" style="left:108px"><div class="member-photo" role="img" aria-label="Portrait photo of team member"></div><h3>Willam Smith</h3><p>Lorem ipsum dolor consectetur adipiscing elited sed do eiusmod tempor incididunt.</p></div>
  <div class="member" style="left:354px"><div class="member-photo" role="img" aria-label="Portrait photo of team member"></div><h3>Willam Smith</h3><p>Lorem ipsum dolor consectetur adipiscing elited sed do eiusmod tempor incididunt.</p></div>
  <div class="member" style="left:600px"><div class="member-photo" role="img" aria-label="Portrait photo of team member"></div><h3>Willam Smith</h3><p>Lorem ipsum dolor consectetur adipiscing elited sed do eiusmod tempor incididunt.</p></div>
  <div class="member" style="left:846px"><div class="member-photo" role="img" aria-label="Portrait photo of team member"></div><h3>Willam Smith</h3><p>Lorem ipsum dolor consectetur adipiscing elited sed do eiusmod tempor incididunt.</p></div>
</section>

<section class="faq">
  <h2 class="section-title two-tone"><span class="a">Frequently</span> <span class="b">Asked Questions</span></h2>
  <div class="faq-item" style="left:117px;top:160px">Lorem ipsum dolor sitconsectetur adipiscing<svg viewBox="0 0 20 20"><circle cx="10" cy="10" r="10" fill="#8a0f96"/><path d="M8 6l4 4-4 4" stroke="#fff" stroke-width="2.4" fill="none"/></svg></div>
  <div class="faq-item" style="left:614px;top:160px">Lorem ipsum dolor sitconsectetur adipiscing<svg viewBox="0 0 20 20"><circle cx="10" cy="10" r="10" fill="#8a0f96"/><path d="M8 6l4 4-4 4" stroke="#fff" stroke-width="2.4" fill="none"/></svg></div>
  <div class="faq-item" style="left:117px;top:238px">Lorem ipsum dolor sitconsectetur adipiscing<svg viewBox="0 0 20 20"><circle cx="10" cy="10" r="10" fill="#8a0f96"/><path d="M8 6l4 4-4 4" stroke="#fff" stroke-width="2.4" fill="none"/></svg></div>
  <div class="faq-item" style="left:614px;top:238px">Lorem ipsum dolor sitconsectetur adipiscing<svg viewBox="0 0 20 20"><circle cx="10" cy="10" r="10" fill="#8a0f96"/><path d="M8 6l4 4-4 4" stroke="#fff" stroke-width="2.4" fill="none"/></svg></div>
  <div class="faq-item active" style="left:117px;top:316px">Lorem ipsum dolor sitconsectetur adipiscing<svg viewBox="0 0 20 20"><circle cx="10" cy="10" r="10" fill="#fff"/><path d="M8 6l4 4-4 4" stroke="#15168c" stroke-width="2.4" fill="none"/></svg></div>
  <div class="faq-item" style="left:614px;top:316px">Lorem ipsum dolor sitconsectetur adipiscing<svg viewBox="0 0 20 20"><circle cx="10" cy="10" r="10" fill="#8a0f96"/><path d="M8 6l4 4-4 4" stroke="#fff" stroke-width="2.4" fill="none"/></svg></div>
  <div class="faq-item" style="left:117px;top:394px">Lorem ipsum dolor sitconsectetur adipiscing<svg viewBox="0 0 20 20"><circle cx="10" cy="10" r="10" fill="#8a0f96"/><path d="M8 6l4 4-4 4" stroke="#fff" stroke-width="2.4" fill="none"/></svg></div>
  <div class="faq-item" style="left:614px;top:394px">Lorem ipsum dolor sitconsectetur adipiscing<svg viewBox="0 0 20 20"><circle cx="10" cy="10" r="10" fill="#8a0f96"/><path d="M8 6l4 4-4 4" stroke="#fff" stroke-width="2.4" fill="none"/></svg></div>
</section>

<section class="support">
  <h2>Support</h2>
  <p>Have questions? Our dedicated support team is here to assist you. Feel free to reach out to info@sharekeel.com for personalised guidance.</p>
  <a class="btn btn-purple" href="#">Contact Us
    <svg viewBox="0 0 16 16"><circle cx="8" cy="8" r="8" fill="#fff"/><path d="M6.5 4.5 10 8l-3.5 3.5" stroke="#8a0f96" stroke-width="2" fill="none"/></svg></a>
</section>

<footer class="site-footer">
  <div class="footer-brand"><span class="dot"></span>ShareKeel</div>
  <div class="footer-col" style="left:371px">
    <h4>COMPANY</h4>
    <ul><li>Home</li><li>About Us</li><li>Our Team</li><li>Key Features</li><li>Why Choose</li><li>Contact Us</li><li>Support</li></ul>
  </div>
  <div class="footer-col contact" style="left:525px">
    <h4>CONTACT US</h4>
    <ul>
      <li><svg viewBox="0 0 12 12"><path d="M2 1h3l1 3-1.5 1a6 6 0 0 0 2.5 2.5L8 6l3 1v3a1 1 0 0 1-1 1A9 9 0 0 1 1 2a1 1 0 0 1 1-1z" fill="#fff"/></svg>+65 9000 4417</li>
      <li><svg viewBox="0 0 12 12"><rect x="0" y="2" width="12" height="8" fill="#fff"/><path d="M0 2l6 4 6-4" stroke="#0b0b0b" fill="none"/></svg>info@sharekeel.com</li>
      <li><svg viewBox="0 0 12 12"><path d="M6 0a4 4 0 0 1 4 4c0 3-4 8-4 8S2 7 2 4a4 4 0 0 1 4-4z" fill="#fff"/><circle cx="6" cy="4" r="1.5" fill="#0b0b0b"/></svg>23,Lorem ipsum dolor<br>consectetur adipiscing</li>
    </ul>
  </div>
  <div class="footer-col news" style="left:703px">
    <h4>SUBSCRIBE TO OUR NEWSLETTER</h4>
    <p>Subscribe to our mailing list to receives daily updates direct to your inbox!</p>
    <div class="news-form"><span>Email Address</span><b>SUBMIT</b></div>
    <div class="social">in</div>
  </div>
  <div class="copyright">Copyrights © ShareKeel 2023 | Allrights Reserved</div>
</footer>

</body>
</html>
```